Web Design Project

We are re-starting this project.

This project is for a totally new look and design of a website for Wablor. www.wablor-demo.net.

Wablor is a naming protocol for physical locations and can be used for fixed and mobile people, places and things. Find your friends, or find a business. Because Wablor locations point to precise geo-physical (GPS) co-ordinates, navigation to a location becomes totally reliable.
Updates

Please see the modified brief for this project

Target Market(s)

Every person and every business can have multiple !Wabs (Wablor locations), so the website needs to be appealing and fun, but easy to use and functional

Industry/Entity Type

Business

Colors
34a6d7

Requirements
Must have
• Uniqueness!

```html
<!DOCTYPE html>
<html lang="en">
<head>
<meta charset="utf-8">
<title>Wablor – Find your friends or find a business</title>
<link rel="stylesheet" href="https://fonts.googleapis.com/css2?family=Lato:ital,wght@0,300;0,400;0,700;0,900;1,400&display=swap">
<style>
:root{
  --blue:#34a6d7;
  --blue-dark:#1d86c4;
  --blue-footer:#1f98d6;
  --tab-dark:#1a6fa8;
  --header-bg:#ececec;
  --nav-bg:#f3f3f3;
  --nav-border:#d2d2d2;
  --text:#333;
  --dark-band:#262626;
  --icon-grey:#8c8c8c;
  --white:#fff;
}
*{box-sizing:border-box;margin:0;padding:0}
html,body{width:898px;height:1200px;overflow:hidden;background:var(--white)}
body{font-family:"Lato",Arial,sans-serif;color:var(--text);position:relative}
a{color:inherit;text-decoration:none}

/* header */
.site-header{position:absolute;left:0;top:0;width:898px;height:98px;background:var(--header-bg);border-top:3px solid var(--blue)}
.brand{position:absolute;left:100px;top:6px;display:flex;align-items:center;gap:6px;color:var(--blue);font-weight:900;font-size:32px;letter-spacing:-0.5px}
.brand-dot{width:13px;height:13px;border-radius:50%;background:var(--blue)}
.account-tab{position:absolute;left:660px;top:0;width:128px;height:24px;background:var(--tab-dark);border-radius:0 0 14px 14px;display:flex;justify-content:center;align-items:center;gap:14px;color:var(--white);font-size:9px;font-weight:700}
.account-tab span{display:flex;align-items:center;gap:4px}

.main-nav{position:absolute;left:98px;top:62px;height:36px;display:flex;border-right:1px solid var(--nav-border)}
.main-nav a{display:flex;align-items:center;justify-content:center;gap:7px;height:36px;background:var(--nav-bg);border-left:1px solid var(--nav-border);border-top:1px solid var(--nav-border);font-size:11.5px;color:#333;text-transform:uppercase}
.main-nav a.is-active{background:var(--blue-dark);color:var(--white);border-color:var(--blue-dark)}
.main-nav svg{width:15px;height:15px;flex:none}

/* hero */
.hero{position:absolute;left:0;top:98px;width:898px;height:426px;background:linear-gradient(180deg,#1f4f95 0%,#4d7fbf 40%,#d48d62 62%,#3a4358 75%,#1c2230 100%)}
.hero-device{position:absolute;left:388px;top:255px;width:392px;height:218px;border-radius:18px;background:linear-gradient(160deg,#3a3a3a,#111)}
.search-panel{position:absolute;left:430px;top:283px;width:314px;height:157px;background:rgba(60,60,60,.88);text-align:center;color:var(--white)}
.search-panel h1{font-weight:300;font-size:26px;line-height:31px;margin-top:18px}
.search-input{display:block;width:218px;height:24px;margin:5px auto 0;background:var(--white);color:#999;font-style:italic;font-size:10px;text-align:left;padding:6px 8px}
.search-button{display:inline-block;margin-top:11px;width:85px;height:24px;line-height:24px;background:var(--blue);color:var(--white);font-size:13px;font-weight:700}

/* features band */
.features{position:absolute;left:0;top:524px;width:898px;height:321px;background:var(--dark-band);text-align:center}
.features h2{color:var(--white);font-weight:400;font-size:20px;margin-top:27px}
.world-map{position:absolute;left:108px;top:78px;width:684px;height:132px;border-radius:4px;background:linear-gradient(180deg,#e6ecfa,#c3d0ef)}
.steps{position:absolute;left:213px;top:240px;width:472px;height:52px}

/* content */
.content{position:absolute;left:0;top:845px;width:898px;height:205px}
.col{position:absolute;top:33px;width:210px}
.col h3{font-size:15px;font-weight:400;color:#222;padding-bottom:5px;border-bottom:2px solid #ddd;position:relative}
.col h3::after{content:"";position:absolute;left:0;bottom:-2px;width:60px;height:2px;background:var(--blue)}
.col h3 em{font-style:normal;color:var(--blue)}
.col-about{left:98px}
.col-about p{font-size:10px;line-height:15.4px;margin-top:8px;color:#333}
.col-about strong{color:var(--blue)}
.read-more{position:absolute;font-size:8px;font-weight:700;color:var(--blue);top:136px;left:0}
.col-faq{left:342px}
.faq-list{list-style:none;margin-top:6px}
.faq-list li{font-size:10px;line-height:14px;padding:4px 0 6px 14px;border-bottom:1px solid #e2e2e2;position:relative}
.faq-list li::before{content:"";position:absolute;left:0;top:8px;border:3px solid transparent;border-left:4px solid #999}
.col-testimonial{left:590px}
.quote{margin-top:10px;background:#f2f2f2;padding:6px 10px 8px 12px;font-style:italic;font-size:9.8px;line-height:15px;color:#333;position:relative}
.quote::after{content:"";position:absolute;left:30px;bottom:-14px;border:7px solid transparent;border-top-color:#f2f2f2;border-left-color:#f2f2f2}
.quote-author{font-size:8px;font-weight:700;color:var(--blue);margin:12px 0 0 70px}
.divider{position:absolute;top:33px;width:1px;height:140px;background:#eee}

/* footer */
.site-footer{position:absolute;left:0;top:1050px;width:898px;height:150px;background:var(--blue-footer);color:var(--white)}
.f-col{position:absolute;top:19px}
.f-col h4{font-weight:400;font-size:13px;padding-bottom:4px;border-bottom:1px solid rgba(255,255,255,.35);text-transform:uppercase}
.quick-links{left:98px;width:138px}
.quick-links ul{list-style:none;display:grid;grid-template-columns:80px 60px;row-gap:12px;margin-top:8px;font-size:10px}
.quick-links li::before{content:"› "}
.contact{left:302px;width:192px}
.contact p{display:flex;gap:10px;font-size:9.5px;line-height:14px;margin-top:10px}
.contact p:first-of-type{margin-top:8px}
.follow{left:532px;width:80px}
.follow ul{list-style:none;margin-top:8px;font-size:10px}
.follow li{display:flex;align-items:center;gap:10px;height:22px}
.social-square{width:13px;height:13px;background:var(--white);opacity:.9}
.f-sep{position:absolute;top:22px;width:1px;height:115px;background:rgba(255,255,255,.2)}
.footer-brand{position:absolute;left:680px;top:38px;width:120px;text-align:center}
.footer-brand .name{display:flex;justify-content:center;align-items:center;gap:5px;font-weight:900;font-size:26px}
.footer-brand .name i{width:11px;height:11px;border-radius:50%;background:var(--white)}
.footer-brand p{font-size:9.5px;line-height:14px;margin-top:6px}
</style>
</head>
<body>

<header class="site-header">
  <div class="brand"><span class="brand-dot"></span>Wablor</div>
  <div class="account-tab">
    <span><svg width="8" height="9" viewBox="0 0 8 9"><rect x="0" y="4" width="8" height="5" fill="#fff"/><path d="M2 4V2.5a2 2 0 0 1 4 0V4" stroke="#fff" fill="none"/></svg>LOGIN</span>
    <span><svg width="9" height="9" viewBox="0 0 9 9"><rect x=".5" y="1.5" width="7" height="7" stroke="#fff" fill="none"/><path d="M3 6l5-5" stroke="#fff"/></svg>SIGN UP</span>
  </div>
  <nav class="main-nav">
    <a class="is-active" href="#" style="width:84px"><svg viewBox="0 0 16 16"><path d="M2 8l6-5 6 5M4 7v6h3v-3h2v3h3V7" fill="#fff"/></svg>Home</a>
    <a href="#" style="width:88px"><svg viewBox="0 0 22 16" style="width:20px"><g fill="#666"><circle cx="5" cy="5" r="2.3"/><circle cx="11" cy="4" r="2.6"/><circle cx="17" cy="5" r="2.3"/><rect x="2" y="8" width="6" height="6"/><rect x="8" y="7.5" width="6" height="7"/><rect x="14" y="8" width="6" height="6"/></g></svg>About</a>
    <a href="#" style="width:83px"><svg viewBox="0 0 16 16"><circle cx="8" cy="8" r="7" fill="#555"/><text x="8" y="12" font-size="10" text-anchor="middle" fill="#fff" font-family="Arial" font-weight="700">?</text></svg>Help</a>
    <a href="#" style="width:102px"><svg viewBox="0 0 18 14" style="width:17px"><rect x="1" y="2" width="16" height="10" fill="#666"/><path d="M1 2l8 6 8-6" stroke="#f3f3f3" fill="none"/></svg>Contact</a>
    <a href="#" style="width:94px"><svg viewBox="0 0 16 16"><rect x="3" y="1" width="10" height="14" fill="none" stroke="#555"/><path d="M5 5h6M5 8h6M5 11h4" stroke="#555"/></svg>Privacy</a>
    <a href="#" style="width:84px"><svg viewBox="0 0 16 16"><rect x="3" y="1" width="10" height="14" fill="#666"/><rect x="5" y="1" width="1.5" height="14" fill="#f3f3f3"/></svg>Terms</a>
    <a href="#" style="width:100px"><svg viewBox="0 0 18 16" style="width:17px"><rect x="1" y="4" width="16" height="10" rx="1" fill="none" stroke="#555" stroke-width="1.5"/><circle cx="9" cy="9" r="3" fill="none" stroke="#555" stroke-width="1.5"/><rect x="6" y="2" width="6" height="2" fill="#555"/></svg>Refunds</a>
    <a href="#" style="width:67px"><svg viewBox="0 0 16 16"><circle cx="8" cy="8" r="7" fill="none" stroke="#555" stroke-width="1.3"/><rect x="7.2" y="7" width="1.6" height="5" fill="#555"/><circle cx="8" cy="4.8" r="1" fill="#555"/></svg>Faq</a>
  </nav>
</header>

<section class="hero" role="img" aria-label="Photo of a city skyline at dusk by the water, with a hand holding a smartphone showing a map"></section>
<div class="hero-device" role="img" aria-label="Smartphone held up in front of the skyline"></div>
<form class="search-panel" action="#">
  <h1>Who Would You Like<br>To Find?</h1>
  <span class="search-input">Enter Your Search</span>
  <span class="search-button">LOOK UP</span>
</form>

<section class="features">
  <h2>FIND YOUR FRIENDS OR FIND A BUSINESS.</h2>
  <div class="world-map" role="img" aria-label="Illustration of a folded dotted world map with two blue location pins"></div>
  <svg class="steps" viewBox="0 0 472 52" aria-hidden="true">
    <g fill="none" stroke="var(--icon-grey)" stroke-width="2.5">
      <rect x="5" y="4" width="24" height="42" rx="3"/>
      <path d="M10 12h14M10 20h14M10 28h10"/>
    </g>
    <path d="M78 30h97M307 30h97" stroke="var(--icon-grey)" stroke-width="2"/>
    <path d="M220 43h42a11 11 0 0 0 0-22 14 14 0 0 0-27-4 10 10 0 0 0-15 8 9 9 0 0 0 0 18z" fill="none" stroke="var(--icon-grey)" stroke-width="2.5"/>
    <g fill="var(--icon-grey)">
      <circle cx="448" cy="8" r="5"/><rect x="442" y="15" width="12" height="20" rx="2"/><rect x="443" y="35" width="4" height="14"/><rect x="449" y="35" width="4" height="14"/>
      <circle cx="462" cy="6" r="5"/><rect x="456" y="13" width="12" height="20" rx="2"/><rect x="457" y="33" width="4" height="14"/><rect x="463" y="33" width="4" height="14"/>
    </g>
  </svg>
</section>

<main class="content">
  <div class="col col-about">
    <h3>ABOUT <em>WABLOR</em></h3>
    <p><strong>Wablor is</strong> an Australian innovation company. Founded in 2012, Wablor has a vision to create the primary geo-physical address protocol in the digital world. Before modern transport, we all knew how to find locations within our community. During the 20th Century,</p>
    <a class="read-more" href="#">READ MORE »</a>
  </div>
  <span class="divider" style="left:323px"></span>
  <div class="col col-faq">
    <h3>FAQ'S</h3>
    <ul class="faq-list">
      <li>Lorem ipsum dolor sit amet conse ctetuears adipiscing elit ?</li>
      <li>Lorem ipsum dolor sit amet conse ctetuerhl adipiscing elit ?</li>
      <li>Lorem ipsum dolor sit amet consectetufer ?</li>
    </ul>
    <a class="read-more" href="#">READ MORE »</a>
  </div>
  <span class="divider" style="left:571px"></span>
  <div class="col col-testimonial">
    <h3>CLIENT <em>TESTIMONIAL</em></h3>
    <blockquote class="quote">“Lorem ipsum dolor sitamet cotuerscing elit sed diam nonummy nibh eod tincidunt ut laoreet dolore magna Lorem ipsum dolor sitamet consetuer adiiscing elit sed diam nonummy nibh euismod”</blockquote>
    <p class="quote-author">Mr. SITAMET CONSETUER</p>
  </div>
</main>

<footer class="site-footer">
  <div class="f-col quick-links">
    <h4>Quick Links</h4>
    <ul>
      <li>Home</li><li>Privacy</li><li>About</li><li>Terms</li><li>Help</li><li>Refunds</li><li>Contact</li><li>Faq</li>
    </ul>
  </div>
  <span class="f-sep" style="left:268px"></span>
  <div class="f-col contact">
    <h4>Contact Information</h4>
    <p><svg width="8" height="11" viewBox="0 0 8 11"><path d="M4 11C1 6 0 5 0 4a4 4 0 0 1 8 0c0 1-1 2-4 7z" fill="#fff"/><circle cx="4" cy="4" r="1.5" fill="var(--blue-footer)"/></svg><span>Suite 7, 44 Harbour Lane<br>Northbay 2099</span></p>
    <p><svg width="10" height="10" viewBox="0 0 10 10"><path d="M2 0l2 2.5-1.2 1.3a6 6 0 0 0 3.4 3.4L7.5 6 10 8 8.5 10C4 10 0 6 0 1.5z" fill="#fff"/></svg><strong>(555) 010-2468</strong></p>
    <p><svg width="11" height="8" viewBox="0 0 11 8"><rect width="11" height="8" fill="#fff"/><path d="M0 0l5.5 4.5L11 0" stroke="var(--blue-footer)" fill="none"/></svg>info@wablor-demo.net</p>
  </div>
  <span class="f-sep" style="left:516px"></span>
  <div class="f-col follow">
    <h4>Follow Us</h4>
    <ul>
      <li><span class="social-square"></span>Friendly</li>
      <li><span class="social-square"></span>Vidcast</li>
      <li><span class="social-square"></span>Chirper</li>
      <li><span class="social-square"></span>Linkwork</li>
    </ul>
  </div>
  <span class="f-sep" style="left:642px"></span>
  <div class="footer-brand">
    <div class="name"><i></i>Wablor</div>
    <p>Copyright © 2014 Wablor.<br>| All Right Reserved</p>
  </div>
</footer>

</body>
</html>
```